Website Design for my Copper Distillation Equipment Business Nature Sciencey Theme

I already have a website www.halvorkettleworks.com and its a pixelhut website builder one. But I cannot get the design right at all. I need this fixed.

I have logo. I need a redesign, for my website, the home page, that maybe I can have something similar in design- I can use as template to copy, for other pages so the whole thing matches? Look at my website so you understand I have a few pages...but most are links. Its a competition. Code has to be easy for me to implement, I am not expert.

Your advice needed..It would be a plus if I can update this myself throughout time. If I could have this explained to me too, the maintenance of it...how would I do this too..etc..pretend I am a child when you explain, if you can. I am not good with this stuff but I am smart and can learn fast.

I want a high end look. Maybe like an ivy league college-y look too, real preppy, chemistry...science-y, nature like is good, leaves, drops water, fields of wheat, lavender, etc.

I want every page to look similar, but the home page is what I want to be the main showpiece,..and I want each page have a little text section, maybe a photos section and a video section, for that market. Like a nice website. If I am not doing this right, let me know. I can work with you. Just help me, please. Let me know if I am doing this right.

When I pick my winning design, for my website, I will hire the artist one-on-one to re-design my shopping cart next. Or if I need additional help with implementing this current design, I can hire the same artist again too. I have a blog that I may want to hire the redesign as well too, but later on. My point is I am not just looking for one project here but I want to follow up with winning artist. So it would be return business for the winner.

I got my logo done here so I am repeat customer. And I have given that winning artist other design work.

Target Market(s)

Moonshine Stills I sell most, Essential Oil Business, Micro and Craft Distilleries, Canna-businesses, Alcohol Fuel

Industry/Entity Type

Business

Number of Pages Required

5+ page

Colors
ec1f27

Requirements
Must have
• The categories for the stills must be prominent and eye catching. The main photo I would like to be naturelike theme, but you can try out different things with me. I am open to ideas and suggestions. I would like this to be implemented easy and fast.
Nice to have
• My logo in it. You can use any of my photos as well from my snapvale account. https://www.snapvale.net/photos/81726354@X07/
• Colors of my Logo...matching design.
• Maybe some basic stock photos you see would match for me..
• Chemistry like symbols for the categories, I love that.

```html
<!DOCTYPE html>
<html lang="en">
<head>
<meta charset="utf-8">
<title>Halvor Kettleworks — Home</title>
<link rel="stylesheet" href="https://fonts.googleapis.com/css2?family=Lato:wght@400;700;900&display=swap">
<style>
:root{
  --red:#ec1f27;
  --ink:#222222;
  --text:#555555;
  --muted:#8a8a8a;
  --line:#dddddd;
  --band:#f0f0f0;
  --white:#ffffff;
  --footer:#1e1e1e;
  --footer-base:#121212;
}
*{box-sizing:border-box;margin:0;padding:0}
html,body{width:1200px;height:2762px;overflow:hidden}
body{position:relative;font-family:'Lato',sans-serif;color:var(--text);background:var(--white)}
.abs{position:absolute}
.hex{clip-path:polygon(50% 0,100% 25%,100% 75%,50% 100%,0 75%,0 25%)}
.hex-icon{position:absolute;width:36px;height:40px;background:var(--red);display:flex;align-items:center;justify-content:center}
.hex-icon.small{width:28px;height:32px}
.hex-icon svg{width:14px;height:14px}

/* header */
.site-header{left:0;top:0;width:1200px;height:111px;background:var(--white)}
.contact-text{font-size:11px;color:var(--red)}
.brand{left:510px;top:22px;width:180px;height:66px;display:flex;align-items:center;justify-content:center;text-align:center;font-weight:900;font-size:17px;line-height:1.15;letter-spacing:1px;color:var(--ink)}
.main-nav{left:0;top:111px;width:1200px;height:43px;background:#ececec}
.main-nav a{position:absolute;top:12px;font-size:11px;color:#666;text-decoration:none;transform:translateX(-50%)}
.main-nav a.active{top:9px;padding:4px 11px;border:1px solid var(--red);color:var(--red);background:var(--white)}

/* hero */
.hero{left:0;top:154px;width:1200px;height:507px;background:linear-gradient(120deg,#3d3f3b 0%,#5a5c56 35%,#2f3a66 60%,#7b7d78 100%)}
.slider-arrow{top:387px}

/* headings */
.section-title{font-size:24px;font-weight:400;color:var(--red);display:flex;align-items:center;gap:6px;white-space:nowrap}
.deco{display:inline-flex;align-items:center}
.deco i{width:8px;height:8px;border-radius:50%;background:var(--red)}
.deco b{width:26px;height:1px;background:var(--red)}
.btn{position:absolute;height:26px;border-radius:13px;background:var(--red);color:var(--white);font-size:10px;font-weight:700;display:flex;align-items:center;justify-content:center;gap:5px;text-transform:uppercase}
.btn.square{border-radius:2px}
.btn .arr{width:10px;height:10px;border-radius:50%;background:var(--white);color:var(--red);font-size:8px;line-height:10px;text-align:center}

/* welcome */
.welcome-photo{left:186px;top:713px;width:191px;height:220px;background:linear-gradient(160deg,#a0663a,#c48a54 50%,#6a7fb2)}
.welcome-title{left:398px;top:706px}
.welcome-copy{left:398px;top:750px;width:594px;font-size:10.5px;line-height:15px;color:#444}
.welcome-copy p+p{margin-top:14px}

/* categories band */
.band{left:0;width:1200px;background:var(--band)}
.category-box{left:186px;top:1040px;width:189px;height:326px;background:var(--white);border:1px solid var(--line);padding:18px 14px 0 14px}
.category-box li{list-style:none;display:flex;align-items:center;gap:10px;height:27px;border-bottom:1px solid var(--line);font-size:10.5px;color:#444}
.category-box li:last-child{border-bottom:none}
.category-box li span{width:9px;height:10px;background:var(--red);flex:none}
.product-card{top:1040px;width:191px;height:326px;background:var(--white);border:1px solid var(--line)}
.product-card .thumb{position:absolute;left:9px;top:9px;width:173px;height:159px}
.product-card h3{position:absolute;left:8px;top:182px;width:175px;text-align:center;color:var(--red);font-size:11.5px;font-weight:900;line-height:18px;text-transform:uppercase}
.product-card p{position:absolute;left:10px;top:228px;width:171px;height:45px;overflow:hidden;font-size:10px;line-height:15px;text-align:justify;color:#555}
.product-card .btn{left:46px;top:282px;width:97px}

/* how it works */
.how-title{left:184px;top:1466px}
.how-copy{left:184px;top:1510px;width:320px;font-size:10px;line-height:16px;color:#777}
.how-copy p+p{margin-top:16px}
.video{left:541px;top:1472px;width:475px;height:269px;background:#111}
.video-frame{position:absolute;left:0;top:16px;width:475px;height:227px;background:linear-gradient(100deg,#3a3a40,#6e6e72 45%,#b9b9b9 80%,#d8d8d8)}
.video-bar{position:absolute;left:0;bottom:0;width:475px;height:26px;background:#1b1b1b;color:#ccc;font-size:9px}
.play{position:absolute;left:212px;top:110px;width:50px;height:36px;border-radius:50%;background:rgba(236,31,39,.9)}
.play:after{content:"";position:absolute;left:21px;top:11px;border-left:12px solid #fff;border-top:7px solid transparent;border-bottom:7px solid transparent}

/* gallery */
.gallery-title{left:0;top:1838px;width:1200px;justify-content:center}
.gallery-item{top:1895px;width:191px;height:223px}

/* news & testimonials */
.news-title{left:184px;top:2214px}
.news-item{left:184px;width:420px;height:60px}
.date-hex{position:absolute;left:0;top:0;width:48px;height:56px;background:var(--red);color:var(--white);text-align:center;padding-top:13px;line-height:1}
.date-hex strong{display:block;font-size:17px;font-weight:400}
.date-hex small{font-size:8px;text-transform:uppercase}
.news-item h4{position:absolute;left:71px;top:6px;font-size:17px;line-height:20px;color:var(--ink);font-weight:700;white-space:nowrap}
.news-item p{position:absolute;left:71px;top:28px;width:340px;font-size:9.5px;line-height:13px;color:#666}
.testi-title{left:600px;top:2214px;width:400px;justify-content:center}
.testi-frame{left:765px;top:2271px;width:94px;height:106px;background:var(--red)}
.testi-photo{left:768px;top:2274px;width:88px;height:100px;background:linear-gradient(170deg,#e8e4e2,#b9b0ae 50%,#4a4a55)}
.testi-name{left:600px;top:2380px;width:424px;text-align:center;font-size:17px;color:var(--red)}
.testi-quote{left:600px;top:2402px;width:424px;text-align:center;font-size:26px;line-height:26px;color:#bbb;font-weight:900}
.testi-copy{left:626px;top:2432px;width:372px;text-align:center;font-size:9.5px;line-height:14px;color:#444}
.dots{left:792px;top:2474px;display:flex;gap:6px}
.dots i{width:9px;height:9px;border-radius:50%;background:var(--red);border:2px solid var(--red)}
.dots i.off{background:var(--white)}

/* footer */
.site-footer{left:0;top:2536px;width:1200px;height:173px;background:var(--footer)}
.footer-contact{left:184px;top:2615px;font-size:12px;color:#ddd}
.footer-contact span{margin:0 14px;color:#aaa}
.footer-brand{left:540px;top:2596px;width:120px;height:52px;display:flex;align-items:center;justify-content:center;text-align:center;font-weight:900;font-size:13px;line-height:1.2;letter-spacing:1px;color:var(--white)}
.footer-base{left:0;top:2709px;width:1200px;height:53px;background:var(--footer-base)}
.footer-links a{position:absolute;top:2730px;font-size:9px;color:#999;text-decoration:none}
.copyright{right:195px;top:2730px;font-size:9px;color:#999}
</style>
</head>
<body>

<header class="site-header abs">
  <div class="hex-icon hex" style="left:182px;top:35px">
    <svg viewBox="0 0 24 24" fill="#fff"><path d="M6.6 10.8a15.1 15.1 0 0 0 6.6 6.6l2.2-2.2c.3-.3.7-.4 1-.2 1.1.4 2.3.6 3.6.6.6 0 1 .4 1 1V20c0 .6-.4 1-1 1A17 17 0 0 1 3 4c0-.6.4-1 1-1h3.5c.6 0 1 .4 1 1 0 1.3.2 2.5.6 3.6.1.3 0 .7-.2 1z"/></svg>
  </div>
  <div class="contact-text abs" style="left:228px;top:49px">555-014-2236</div>
  <div class="hex-icon hex" style="left:307px;top:35px">
    <svg viewBox="0 0 24 24" fill="none" stroke="#fff" stroke-width="2"><rect x="3" y="5" width="18" height="14"/><path d="M3 6l9 7 9-7"/></svg>
  </div>
  <div class="contact-text abs" style="left:352px;top:49px">office@halvorkettleworks.com</div>

  <div class="brand abs">HALVOR<br>KETTLEWORKS</div>

  <div class="hex-icon hex" style="left:855px;top:35px"></div>
  <div class="hex-icon hex" style="left:896px;top:35px"></div>
  <div class="hex-icon hex" style="left:939px;top:35px"></div>
  <div class="hex-icon hex" style="left:980px;top:35px"></div>
</header>

<nav class="main-nav abs">
  <a class="active" href="#" style="left:217px">Home</a>
  <a href="#" style="left:318px">About Us</a>
  <a href="#" style="left:429px">Contact Us</a>
  <a href="#" style="left:533px">Photo</a>
  <a href="#" style="left:624px">Video</a>
  <a href="#" style="left:715px">Shop</a>
  <a href="#" style="left:803px">Blog</a>
  <a href="#" style="left:892px">Books</a>
  <a href="#" style="left:983px">Links</a>
</nav>

<section class="hero abs" role="img" aria-label="Slide photo: distiller holding a flask of golden oil in front of a chalkboard"></section>
<div class="hex-icon hex slider-arrow" style="left:21px">
  <svg viewBox="0 0 24 24" fill="none" stroke="#fff" stroke-width="3"><path d="M15 5l-7 7 7 7"/></svg>
</div>
<div class="hex-icon hex slider-arrow" style="left:1141px">
  <svg viewBox="0 0 24 24" fill="none" stroke="#fff" stroke-width="3"><path d="M9 5l7 7-7 7"/></svg>
</div>

<section class="welcome">
  <div class="welcome-photo hex abs" role="img" aria-label="Photo: distiller working at a copper still in a kitchen"></div>
  <h2 class="welcome-title section-title abs">Welcome To Our Website. <span class="deco"><i></i><b></b></span></h2>
  <div class="welcome-copy abs">
    <p>Are you looking for a Moonshine Still? Are you a Lavender Farm? Are you wanting to distill Essential Oils on your farm and make Hydrosols too? Do you want to make an Herbal Extraction or Tincture? Do you want to start a Home Business? Are you a Micro (small) Distillery wanting a Set up? Are you a Race Car driver looking for alternative ways to get your Ethanol? Are you a Prepper? Are you interested in Making Alcohol in times of Survival? Do you need clean radiation free Water for your community? Do you want to support Local Farmers, get back to the Source and Nature? Are you a Canna business or 502?</p>
    <p>My Dream Customer is someone who believes they cannot, but does it anyways and finds out they can! And then they go and teach someone....that is a gift that keeps on giving. Those are the results I want to give. Taking a liquid, turning it into a vapor and then back into a liquid. That is all you need to know.</p>
  </div>
  <div class="btn" style="left:398px;top:907px;width:113px">Learn More <span class="arr">›</span></div>
</section>

<section class="band abs" style="top:985px;height:433px"></section>
<ul class="category-box abs">
  <li><span class="hex"></span>Stills</li>
  <li><span class="hex"></span>Essential Oils</li>
  <li><span class="hex"></span>Alcohol Fuel</li>
  <li><span class="hex"></span>Cannabis</li>
  <li><span class="hex"></span>Boilers</li>
  <li><span class="hex"></span>Home Distillers</li>
  <li><span class="hex"></span>Vodka Still</li>
  <li><span class="hex"></span>Heat Control</li>
  <li><span class="hex"></span>Distillery</li>
  <li><span class="hex"></span>Kits</li>
  <li><span class="hex"></span>Parts</li>
</ul>

<article class="product-card abs" style="left:398px">
  <div class="thumb" role="img" aria-label="Photo: copper and steel home stills outdoors" style="background:linear-gradient(180deg,#3f6b2e,#9aa0a0 55%,#6b5a3a)"></div>
  <h3>Home Distillers! We sell copper stills.</h3>
  <p>Lorem ipsum dolor sit amet, consectetuer adipiscing elit, sed diam nonummy nibh euismod tincidunt ut laoreet dolore.</p>
  <div class="btn square">Read More <span class="arr">›</span></div>
</article>
<article class="product-card abs" style="left:611px">
  <div class="thumb" role="img" aria-label="Photo: micro distillery copper still with control panel" style="background:linear-gradient(180deg,#6f8f5a,#b8b8b0 50%,#3a4a8a)"></div>
  <h3>Micro Distillery Equipm-<br>ent copper still for sale</h3>
  <p>Lorem ipsum dolor sit amet, consectetuer adipiscing elit, sed diam nonummy nibh euismod tincidunt ut laoreet dolore.</p>
  <div class="btn square">Read More <span class="arr">›</span></div>
</article>
<article class="product-card abs" style="left:825px">
  <div class="thumb" role="img" aria-label="Photo: herbal extract in a flask held up to a chalkboard" style="background:linear-gradient(150deg,#555a55,#c9b24a 40%,#3a4a8a 70%,#777)"></div>
  <h3>Witch herbal extractor makecannabis oil with</h3>
  <p>Lorem ipsum dolor sit amet, consectetuer adipiscing elit, sed diam nonummy nibh euismod tincidunt ut laoreet dolore.</p>
  <div class="btn square">Read More <span class="arr">›</span></div>
</article>

<section class="how">
  <h2 class="how-title section-title abs">How It Works <span class="deco"><i></i><b></b></span></h2>
  <div class="how-copy abs">
    <p>Lorem ipsum dolor sit amet, consectetuer adipiscing elit, sed diam nonummy nibh euismod tincidunt ut laoreet dolore magna aliquam erat volutpat. Ut wisi enim ad minim veniam, quis nostrud exerci tation ullamcorper suscipit lobortis nisl ut aliquip ex ea commodo consequat.</p>
    <p>Duis autem vel eum iriure dolor in hendrerit in vulputate velit esse molestie consequat, vel illum dolore eu feugiat nulla facilisis at vero eros et accumsan et iusto odio dignissim qui blandit praesent luptatum zzril delenit augue.</p>
  </div>
  <div class="btn square" style="left:184px;top:1707px;width:98px;height:34px">Read More</div>
  <div class="video abs">
    <div class="video-frame" role="img" aria-label="Video still: two men standing beside a copper still in a workshop"></div>
    <div class="play"></div>
    <div class="video-bar"><span style="position:absolute;left:60px;top:8px">00:00</span></div>
  </div>
</section>

<section class="band abs" style="top:1793px;height:375px"></section>
<h2 class="gallery-title section-title abs"><span class="deco"><b></b><i></i></span> Gallery <span class="deco"><i></i><b></b></span></h2>
<div class="gallery-item hex abs" style="left:186px;background:linear-gradient(150deg,#5a4a2a,#a89a5a 50%,#2f3f2f)" role="img" aria-label="Gallery photo: man looking through a glass of oil"></div>
<div class="gallery-item hex abs" style="left:398px;background:linear-gradient(150deg,#e4e4e0,#cfc86a 55%,#6f8a4a)" role="img" aria-label="Gallery photo: jar of golden essential oil"></div>
<div class="gallery-item hex abs" style="left:611px;background:linear-gradient(150deg,#5f7f4a,#c9c2bc 50%,#8a5a3a)" role="img" aria-label="Gallery photo: man standing beside a copper still"></div>
<div class="gallery-item hex abs" style="left:825px;background:linear-gradient(150deg,#6f9f4a,#3a4a9a 45%,#8fbf5a)" role="img" aria-label="Gallery photo: still with control box in a garden"></div>

<section class="news">
  <h2 class="news-title section-title abs">Letest News <span class="deco"><i></i><b></b></span></h2>
  <div class="news-item abs" style="top:2270px">
    <div class="date-hex hex"><strong>06</strong><small>May</small></div>
    <h4>Lorem ipsum dolor sit amet, consectetuer</h4>
    <p>sed diam nonummy nibh euismod tincidunt ut laoreet dolore magna aliquam erat volutpat. Ut wisi enim ad minim veniam.</p>
  </div>
  <div class="news-item abs" style="top:2348px">
    <div class="date-hex hex"><strong>15</strong><small>Jan</small></div>
    <h4>Lorem ipsum dolor sit amet, consectetuer</h4>
    <p>sed diam nonummy nibh euismod tincidunt ut laoreet dolore magna aliquam erat volutpat. Ut wisi enim ad minim veniam.</p>
  </div>
  <div class="news-item abs" style="top:2426px">
    <div class="date-hex hex"><strong>26</strong><small>Feb</small></div>
    <h4>Lorem ipsum dolor sit amet, consectetuer</h4>
    <p>sed diam nonummy nibh euismod tincidunt ut laoreet dolore magna aliquam erat volutpat. Ut wisi enim ad minim veniam.</p>
  </div>
</section>

<section class="testimonials">
  <h2 class="testi-title section-title abs"><span class="deco"><b></b><i></i></span> Testimonials <span class="deco"><i></i><b></b></span></h2>
  <div class="testi-frame hex abs"></div>
  <div class="testi-photo hex abs" role="img" aria-label="Portrait photo of the customer"></div>
  <div class="testi-name abs">Marisol Quenby</div>
  <div class="testi-quote abs">&ldquo;</div>
  <p class="testi-copy abs">Lorem ipsum dolor sit amet, consectetuer adipiscing elit, sed diam nonummy nibh euismod tincidunt ut laoreet dolore magna aliquam erat volutpat.</p>
  <div class="dots abs"><i></i><i class="off"></i><i></i></div>
</section>

<footer>
  <div class="site-footer abs"></div>
  <div class="footer-contact abs">office@halvorkettleworks.com<span>|</span>555-014-2236</div>
  <div class="footer-brand abs">HALVOR<br>KETTLEWORKS</div>
  <div class="hex-icon hex small" style="left:826px;top:2606px"></div>
  <div class="hex-icon hex small" style="left:867px;top:2606px"></div>
  <div class="hex-icon hex small" style="left:908px;top:2606px"></div>
  <div class="hex-icon hex small" style="left:949px;top:2606px"></div>
  <div class="hex-icon hex small" style="left:990px;top:2606px"></div>
  <div class="footer-base abs"></div>
  <nav class="footer-links">
    <a href="#" style="left:184px">Home</a>
    <a href="#" style="left:244px">About Us</a>
    <a href="#" style="left:317px">Shop Now</a>
    <a href="#" style="left:393px">Gallery</a>
    <a href="#" style="left:459px">Book</a>
    <a href="#" style="left:514px">Contact Us</a>
  </nav>
  <div class="copyright abs">© 2015 halvorkettleworks.com &nbsp;|&nbsp; All Rights Reserved.</div>
</footer>

</body>
</html>
```